Local fast-growing company in the service sector

We are looking for a modern business card design, which should also appear on our letterheads

Target Market(s)

Private and industrial sectors

Contact Information for Business Card

Vorname Name
Lindkofer Str. 18
71468 Waiblingen
Tel.: 07163-418259-0
Name@kovaltec-pbz.de

Colors
9d9d9d
919191
aaaaaa

Requirements
Must have
• The logo (file) in silver

```html
<!DOCTYPE html>
<html lang="de">
<head>
<meta charset="utf-8">
<title>KPBZ Visitenkarte</title>
<link href="https://fonts.googleapis.com/css2?family=Arimo:wght@400;700&display=swap" rel="stylesheet">
<style>
  :root {
    --backdrop: #2e2e2e;
    --card-white: #f7f7f7;
    --silver: #9d9d9d;
    --silver-dark: #919191;
    --silver-light: #aaaaaa;
    --ink: #1a1a1a;
    --ink-soft: #2b2b2b;
    --title-light: #e6e6e6;
  }
  * { margin: 0; padding: 0; box-sizing: border-box; }
  html, body { width: 1200px; height: 997px; overflow: hidden; }
  body {
    background: var(--backdrop);
    font-family: "Arimo", Arial, sans-serif;
    position: relative;
  }
  .business-card {
    position: absolute;
    left: 150px;
    top: 241px;
    width: 900px;
    height: 514px;
    background: linear-gradient(180deg, #ffffff 0%, var(--card-white) 60%);
    overflow: hidden;
    box-shadow: 0 18px 40px rgba(0,0,0,0.5);
  }
  .card-shapes { position: absolute; inset: 0; width: 900px; height: 514px; }
  .brand {
    position: absolute;
    left: 270px;
    top: 80px;
    display: flex;
    align-items: center;
    gap: 22px;
  }
  .brand-dot {
    width: 70px; height: 70px;
    border-radius: 50%;
    background: var(--silver);
  }
  .brand-name {
    font-weight: 700;
    font-size: 88px;
    letter-spacing: 2px;
    color: var(--silver);
    line-height: 1;
  }
  .holder {
    position: absolute;
    left: 95px;
    top: 380px;
  }
  .holder-name {
    font-weight: 700;
    font-size: 28px;
    color: var(--ink);
    letter-spacing: 0.5px;
  }
  .holder-title {
    font-weight: 700;
    font-size: 22px;
    color: var(--title-light);
    margin-top: 4px;
    letter-spacing: 0.5px;
  }
  .divider {
    position: absolute;
    left: 420px;
    top: 290px;
    width: 2px;
    height: 150px;
    background: var(--ink-soft);
  }
  .contact-list {
    position: absolute;
    left: 450px;
    top: 295px;
    list-style: none;
  }
  .contact-item {
    display: flex;
    align-items: center;
    gap: 16px;
    height: 42px;
    font-size: 24px;
    color: var(--ink);
    letter-spacing: 0.5px;
  }
  .contact-icon { width: 22px; height: 22px; flex: none; }
</style>
</head>
<body>
  <div class="business-card">
    <svg class="card-shapes" viewBox="0 0 900 514" aria-hidden="true">
      <path class="silver-band" d="M0 514 L0 420 Q 360 180 900 200 L900 514 Z" fill="#a3a3a3"/>
      <path class="swoosh" d="M30 410 Q 380 165 900 190 L900 198 Q 390 180 30 410 Z" fill="#111"/>
    </svg>

    <div class="brand">
      <span class="brand-dot"></span>
      <span class="brand-name">KPBZ</span>
    </div>

    <div class="holder">
      <p class="holder-name">JONAS M. KESSLER</p>
      <p class="holder-title">PRESIDENT &amp; CEO</p>
    </div>

    <div class="divider"></div>

    <ul class="contact-list">
      <li class="contact-item">
        <svg class="contact-icon" viewBox="0 0 24 24" aria-hidden="true"><path d="M6 3 L10 3 L11 8 L8 10 Q10 14 14 16 L16 13 L21 14 L21 18 Q21 21 18 21 Q4 19 3 6 Q3 3 6 3 Z" fill="#555"/></svg>
        <span>07163-418259-0</span>
      </li>
      <li class="contact-item">
        <svg class="contact-icon" viewBox="0 0 24 24" aria-hidden="true"><rect x="2" y="5" width="20" height="14" fill="#555"/><path d="M2 5 L12 13 L22 5" stroke="#ddd" stroke-width="1.6" fill="none"/></svg>
        <span>Name@kovaltec-pbz.de</span>
      </li>
      <li class="contact-item">
        <svg class="contact-icon" viewBox="0 0 24 24" aria-hidden="true"><path d="M12 2 C7 2 4.5 5.5 4.5 9 C4.5 14 12 22 12 22 C12 22 19.5 14 19.5 9 C19.5 5.5 17 2 12 2 Z" fill="#555"/><circle cx="12" cy="9" r="3" fill="#ddd"/></svg>
        <span>Lindkofer Str. 18, 71468 Waiblingen</span>
      </li>
    </ul>
  </div>
</body>
</html>
```